Elegant and modern body scrub for organic junkies

I need a package design for my new company based out of Austin, Texas. We are focused on cruelty free and all natural and organic products. Our deign needs to be able to have the information we require on it, while still appearing very clean and captivating. Our initial product is a clear skin body scrub, intended for people with problematic skin. Our target market is women and we want to show elegance, without appearing "high end."
Updates

Reason: I want to allot more time for certain designers to submit edits. Last minute proposals have been appealing

Target Market(s)

Women. Organic and holistic minded. Natural beauty lovers.

Industry/Entity Type

Skin Care Product

Font styles to use
Script
Other font styles liked:
• AmericanTypewriter, Beautifulflaws, courier, caviarDreams-bold

Colors
000000
ffc214
ffffff
fece3e
fbee3e

Requirements
Must have
• Must be designed in Adobe Illustrator.
• The photo titled “structure for oz and grams” -That needs to be included at the bottom of 1B. I like the horizontal and vertical bar that separate the two. I want that.
• Color Inspiration - The photo titled “venra color inspiration” and “color combo inspiration” are the colors I want. BLACK, GOLD, WHITE. I want the label background black and the writing in white with some gold somewhere on it. My logo is going to be a golden elephant.
• The photos titled “I like how clean this looks” and “I also like how clean this looks” - I want 1B to look super clean. I don’t want a lot of information in this box. I want simple and clean. This is where the logo and brand name will go.
• Logo - A golden elephant. I want it to be gold and geometric. There can be dimension like this elephant example on the left of the 1B description. I want the trunk to be facing to the left and the trunk needs to be raised overhead and touching the animal's forehead.
• The photo titled “sideways writing and silver rim” - I want 1C to be written sideways like this. My text will be much more extensive so the font won’t be able to be so big.
Nice to have
• The photo titled “sideways writing and silver rim” - I want 1C to be written sideways like this. My text will be much more extensive so the font won’t be able to be so big. I also REALLY like how this label is rimmed in silver, but I would want gold. This is not mandatory, but I really like this.
• The photo titled “melted honey” - This is another option I really like. The gold that looks like honey dripping on the label is really cool. Not mandatory, but I really liked that. I also like the craft background on this.
• Color Inspiration - The photo titled “color inspiration” and “another color inspiration” is an option I would also like to see. Rather than black, I’d like to see what it would ALSO look like with a navy background. NAVY, GOLD, WHITE, maybe black somewhere.
Should not have
• Colorful patterns or excessive info in section 1B.

```html
<!DOCTYPE html>
<html lang="en">
<head>
<meta charset="utf-8">
<title>Clear Skin Body Scrub – Label</title>
<link href="https://fonts.googleapis.com/css2?family=Raleway:wght@300;400;600;700&family=Open+Sans:wght@400;600;700&display=swap" rel="stylesheet">
<style>
  :root {
    --black: #000000;
    --gold: #ffc214;
    --gold-soft: #fece3e;
    --gold-deep: #c9962a;
    --white: #ffffff;
    --ink: #1a1a1a;
  }
  * { box-sizing: border-box; margin: 0; padding: 0; }
  html, body { width: 1200px; height: 191px; overflow: hidden; background: var(--white); }
  .label { position: relative; width: 1200px; height: 191px; font-family: "Open Sans", sans-serif; color: var(--ink); }

  /* Left info panel */
  .info-panel { position: absolute; left: 0; top: 0; width: 335px; height: 191px; background: var(--white); }
  .claims { display: flex; height: 46px; }
  .claim { display: flex; align-items: center; justify-content: center; text-align: center;
           background: var(--gold); color: var(--ink); font-size: 7px; font-weight: 600; line-height: 1.25;
           padding: 0 4px; border-right: 1px solid var(--white); }
  .claim--cruelty { width: 78px; }
  .claim--organic { width: 80px; background: var(--white); border: 1px solid var(--gold); }
  .claim--free { flex: 1; border-right: 0; }
  .usage { padding: 9px 8px 0 8px; font-size: 5.6px; line-height: 1.45; }
  .usage p + p { margin-top: 9px; }
  .usage strong { font-weight: 700; }
  .recycle { position: absolute; left: 8px; bottom: 10px; display: flex; align-items: center; gap: 16px; font-size: 6.4px; }

  /* Front panel */
  .front-panel { position: absolute; left: 335px; top: 0; width: 435px; height: 191px; background: var(--black); }
  .elephant-mark { position: absolute; left: 100px; top: 10px; width: 150px; height: 135px;
                   background: radial-gradient(ellipse at 55% 45%, var(--gold-soft), var(--gold-deep) 70%, transparent 71%); opacity: .9; }
  .brand-name { position: absolute; left: 250px; top: 8px; font-family: "Raleway", sans-serif; font-weight: 300;
                font-size: 25px; color: var(--gold); letter-spacing: .3px; }
  .product-name { position: absolute; right: 68px; top: 78px; text-align: right; font-family: "Raleway", sans-serif;
                  font-weight: 300; font-size: 15px; line-height: 1.25; color: var(--white); letter-spacing: .3px; }
  .net-weight { position: absolute; left: 155px; top: 158px; width: 170px; height: 28px; border-top: 1px solid var(--white);
                display: flex; color: var(--white); font-size: 7px; }
  .net-weight span { flex: 1; text-align: center; padding-top: 9px; }
  .net-weight span:first-child { flex: .7; border-right: 1px solid var(--white); }

  /* Side panel */
  .side-panel { position: absolute; left: 770px; top: 0; width: 430px; height: 191px; background: var(--white); overflow: hidden; }
  .side-copy { writing-mode: vertical-rl; transform: rotate(180deg); width: 430px; height: 191px;
               padding: 10px 12px; font-size: 5.6px; line-height: 1.5; }
  .side-brand { font-family: "Raleway", sans-serif; font-weight: 400; font-size: 34px; color: var(--gold); line-height: 1.1; margin-left: 8px; }
  .side-tagline { font-weight: 700; font-size: 7.5px; line-height: 1.35; margin-left: 14px; }
  .side-copy p { margin-left: 10px; }
  .side-copy .emphasis { font-weight: 700; font-size: 6.6px; text-align: center; margin-left: 40px; }
  .side-copy .fine { font-size: 4.6px; }
</style>
</head>
<body>
<div class="label">

  <section class="info-panel">
    <div class="claims">
      <div class="claim claim--cruelty">Cruelty Free<br>Never Tested on Animals</div>
      <div class="claim claim--organic">Organic<br>Ingredients</div>
      <div class="claim claim--free">FREE OF: Parabens, Synthetics, Fragrance, GMOs, or any other fakeness.</div>
    </div>
    <div class="usage">
      <p><strong>Directions:</strong> Shake well before use. Gently massage scrub in circular motions over wet skin (not face). Pay special attention to rough or dry patches. After use, a residual layer of oil will remain on skin. Rinse thoroughly and pat dry with towel. Skin will feel elegantly soft and nourished. Avoid use on freshly shaven or broken skin.</p>
      <p><strong>Caution:</strong> Oils in product may leave shower or tub surfaces slippery. Not intended for facial use. Essential oils or use on freshly shaven skin may cause skin irritation. External use only.</p>
    </div>
    <div class="recycle">
      <svg width="24" height="22" viewBox="0 0 24 22" aria-hidden="true">
        <g fill="none" stroke="#1a1a1a" stroke-width="2.4" stroke-linejoin="round">
          <path d="M9 3 L12 1 L15 6"/><path d="M18 9 L21 15 L15 15"/><path d="M7 19 L2 15 L6 9"/>
        </g>
        <g fill="#1a1a1a"><path d="M13 4 L17 2 L17 7 Z"/><path d="M14 12 L14 18 L10 15 Z"/><path d="M4 9 L8 9 L6 5 Z"/></g>
      </svg>
      <span>Please recycle. I want to come back as a solar panel.</span>
    </div>
  </section>

  <section class="front-panel">
    <div class="elephant-mark" role="img" aria-label="Geometric golden elephant logo with raised trunk facing left"></div>
    <h1 class="brand-name">Brand Name</h1>
    <p class="product-name">Clear Skin<br>Body Scrub</p>
    <div class="net-weight"><span>12oz</span><span>340 g</span></div>
  </section>

  <section class="side-panel">
    <div class="side-copy">
      <h2 class="side-brand">Brand Name</h2>
      <p class="side-tagline">Made with naturally derived<br>ingredients only.</p>
      <p>The combination of ingredients in this loving scrub were chosen with problematic body skin in mind. Cleanse with gentle exfoliation from sea salt and sugar, while minerals in Dead Sea salt help balance oil, calm irritation and support clear skin.</p>
      <p>Pink salt is rapidly absorbed into the skin, clearing pores and refining the texture, tone and overall look of the skin while reducing inflammation.</p>
      <p>This loving essential oil blend helps fight acne, soothe redness and regulate sebaceous glands. Tea tree and lavender bring antibacterial and calming benefits to skin, keeping it clear and balanced from day to day.</p>
      <p class="emphasis">Each of these ingredients plays an essential role in this scrub, gently fighting problem skin and leaving you polished, soft and ready to glow.</p>
      <p class="fine">Ingredients: Dead Sea Salt, Pink Himalayan Salt, Cane Sugar, Coconut Oil, Jojoba Oil, Tea Tree Oil, Lavender Oil, Vitamin E. Austin, TX.</p>
    </div>
  </section>

</div>
</body>
</html>
```